Accounting business needs a fridge magnet design

I need a business card size design to be used as a fridge magnet.
It will need to be vertical not horizontal and it will have my logo and the services I provide listed below it.
It needs to be pleasing to the eye and catch peoples attention.
I have uploaded my current business card as a reference.
It can look totally different though, i am open to new ideas.

It will need to say:

Specialising in:
*Small Business Taxation
*Company & Trust Returns
*Financial Statements
*Partnership Taxation
*BAS preparation/lodgement
*Capital Gains Tax
*Business Start Ups
*Business Structuring
*Tax Planning

```html
<!DOCTYPE html>
<html lang="en">
<head>
<meta charset="utf-8">
<title>Northvale Accounts – Fridge Magnet</title>
<link href="https://fonts.googleapis.com/css2?family=Montserrat:wght@300;500&family=Oswald:wght@600&display=swap" rel="stylesheet">
<style>
  :root{
    --backdrop:#2587ca;
    --card-white:#ffffff;
    --navy:#13296a;
    --navy-light:#1f3a7e;
    --stripe-blue:#1f86cf;
    --ink:#1d1d1d;
    --badge-sky:#1bb5ea;
    --badge-blue:#1d5fa8;
    --badge-lime:#a6cf2a;
    --text-light:#ffffff;
  }
  *{margin:0;padding:0;box-sizing:border-box}
  html,body{width:1200px;height:1200px;overflow:hidden}
  body{background:var(--backdrop);display:flex;align-items:center;justify-content:center}
  .magnet{
    width:640px;height:1040px;background:var(--card-white);
    position:relative;overflow:hidden;
    box-shadow:0 12px 30px rgba(0,0,0,.25);
  }
  .brand{position:absolute;top:150px;left:0;right:0;display:flex;justify-content:center;align-items:center;gap:18px}
  .brand-dot{width:40px;height:40px;border-radius:50%;background:var(--navy);flex:none}
  .brand-name{font-family:'Montserrat',sans-serif;font-weight:500;font-size:44px;color:var(--navy);letter-spacing:1px;white-space:nowrap}
  .credentials{position:absolute;top:340px;left:0;right:0;display:flex;justify-content:center;align-items:flex-start;gap:52px}
  .badge-partner{width:94px;height:94px;border-radius:50%;background:var(--badge-sky)}
  .badge-member{width:86px;height:86px;background:var(--badge-blue);margin-top:4px}
  .badge-registered{display:flex;flex-direction:column;align-items:center}
  .badge-registered .seal{width:94px;height:94px;border-radius:50%;background:var(--badge-lime)}
  .badge-registered .agent-no{font-family:'Montserrat',sans-serif;font-weight:300;font-size:11px;color:var(--ink);text-align:center;margin-top:4px;line-height:1.2}
  .divider-stripe{position:absolute;top:510px;left:0;right:0;height:16px;background:var(--stripe-blue)}
  .services-panel{
    position:absolute;top:540px;left:0;right:0;bottom:0;
    background:linear-gradient(160deg,var(--navy-light),var(--navy));
    color:var(--text-light);padding:38px 36px 0;
  }
  .services-title{font-family:'Oswald',sans-serif;font-weight:600;font-size:34px;text-align:center;letter-spacing:.5px}
  .services-list{display:flex;justify-content:space-between;margin-top:22px}
  .services-list ul{list-style:none;font-family:'Oswald',sans-serif;font-weight:600;font-size:21px;line-height:1.5;text-transform:uppercase;white-space:nowrap}
  .services-list li::before{content:"•";margin-right:6px}
  .contact-rule{height:1px;background:rgba(255,255,255,.55);margin:26px 0 22px}
  .contact{font-family:'Montserrat',sans-serif;font-weight:300;font-size:22px}
  .contact-row{display:flex;align-items:center;gap:12px;margin-bottom:14px;white-space:nowrap}
  .contact-row svg{width:22px;height:22px;flex:none}
  .contact-pair{display:flex;gap:32px}
</style>
</head>
<body>
  <div class="magnet">
    <div class="brand">
      <div class="brand-dot"></div>
      <div class="brand-name">Northvale Accounts</div>
    </div>

    <div class="credentials">
      <div class="badge-partner" role="img" aria-label="Accounting software partner badge"></div>
      <div class="badge-member" role="img" aria-label="Professional accounting body membership badge"></div>
      <div class="badge-registered">
        <div class="seal" role="img" aria-label="Registered tax agent seal"></div>
        <div class="agent-no">Tax agent<br>31850297</div>
      </div>
    </div>

    <div class="divider-stripe"></div>

    <section class="services-panel">
      <h2 class="services-title">SPECIALISING IN:</h2>
      <div class="services-list">
        <ul>
          <li>Small Business Taxation</li>
          <li>Company &amp; Trust Returns</li>
          <li>Financial Statements</li>
          <li>Partnership Taxation</li>
        </ul>
        <ul>
          <li>BAS Preparation/Lodgement</li>
          <li>Capital Gains Tax</li>
          <li>Business Start Ups</li>
          <li>Business Structuring</li>
          <li>Tax Planning</li>
        </ul>
      </div>

      <div class="contact-rule"></div>

      <div class="contact">
        <div class="contact-pair">
          <div class="contact-row">
            <svg viewBox="0 0 24 24"><path fill="#fff" d="M6.6 10.8a15 15 0 0 0 6.6 6.6l2.2-2.2c.3-.3.7-.4 1-.2 1.1.4 2.3.6 3.6.6.6 0 1 .4 1 1V20c0 .6-.4 1-1 1A17 17 0 0 1 3 4c0-.6.4-1 1-1h3.5c.6 0 1 .4 1 1 0 1.3.2 2.5.6 3.6.1.3 0 .7-.2 1z"/></svg>
            <span>0400 582 316</span>
          </div>
          <div class="contact-row">
            <svg viewBox="0 0 24 24"><rect x="2" y="5" width="20" height="14" fill="#fff"/><path d="M2 5l10 8 10-8M2 19l7-7M22 19l-7-7" stroke="#13296a" stroke-width="1.6" fill="none"/></svg>
            <span>sam@northvale.com.au</span>
          </div>
        </div>
        <div class="contact-row">
          <svg viewBox="0 0 24 24" fill="none" stroke="#fff" stroke-width="1.6"><circle cx="12" cy="12" r="10"/><ellipse cx="12" cy="12" rx="4.5" ry="10"/><path d="M2 12h20M4 7h16M4 17h16"/></svg>
          <span>www.northvale.com.au</span>
        </div>
      </div>
    </section>
  </div>
</body>
</html>
```